Business Card for boutique psychology business

Business card for boutique psychology practice in Melbourne. I want them to be relatively simply with the logo and backing colour taking up the front side. Then, text on the back, with my name; professional title (Clinical Psychologist); website - torvinpsychology.com.au; email: hello@torvinpsychology.com.au; insta: @torvin.psychology.emdr
Back should also have the words: Connect. Integrate. Evolve
Fonts used for logo are: Mikea Demo and Gotham Medium. Use something for back text that will compliment these.
Brand colours uploaded below. I'd like to see options in both olive and blush.

```html
<!DOCTYPE html>
<html lang="en">
<head>
<meta charset="utf-8">
<title>Torvin Psychology – Business Card</title>
<link rel="stylesheet" href="https://fonts.googleapis.com/css2?family=Arimo:wght@400;700&family=Montserrat:wght@300;500&family=Libre+Baskerville:wght@700&display=swap">
<style>
  :root {
    --olive: #434329;
    --blush: #ecc9b8;
    --backdrop: #f2f2f2;
  }
  * { margin: 0; padding: 0; box-sizing: border-box; }
  html, body {
    width: 1199px;
    height: 1200px;
    overflow: hidden;
    background: var(--backdrop);
  }
  .card {
    position: absolute;
    left: 210px;
    top: 378px;
    width: 780px;
    height: 444px;
    background: var(--olive);
    overflow: hidden;
    color: var(--blush);
  }
  .card-arc {
    position: absolute;
    inset: 0;
    width: 780px;
    height: 444px;
  }
  .brand {
    position: absolute;
    left: 20px;
    top: 168px;
    width: 250px;
    text-align: center;
  }
  .brand-name {
    font-family: "Montserrat", sans-serif;
    font-weight: 300;
    font-size: 66px;
    line-height: 1;
    letter-spacing: 1px;
  }
  .brand-descriptor {
    font-family: "Montserrat", sans-serif;
    font-weight: 500;
    font-size: 14px;
    margin-top: 6px;
    letter-spacing: 0.3px;
  }
  .tagline {
    position: absolute;
    left: 20px;
    top: 338px;
    width: 260px;
    text-align: center;
    font-family: "Libre Baskerville", serif;
    font-weight: 700;
    font-size: 16px;
    letter-spacing: -0.3px;
  }
  .person {
    position: absolute;
    left: 300px;
    top: 78px;
    width: 410px;
    text-align: center;
  }
  .person-name {
    font-family: "Arimo", sans-serif;
    font-weight: 700;
    font-size: 45px;
    line-height: 1.1;
  }
  .person-title {
    font-family: "Montserrat", sans-serif;
    font-weight: 500;
    font-size: 17px;
    letter-spacing: 4.6px;
    margin-top: 4px;
  }
  .contact {
    position: absolute;
    font-family: "Arimo", sans-serif;
    font-size: 26px;
    line-height: 1;
    white-space: nowrap;
    transform: translateY(-50%);
  }
  .contact-web   { left: 342px; top: 204px; }
  .contact-email { left: 361px; top: 274px; }
  .contact-social{ left: 376px; top: 331px; }
</style>
</head>
<body>
  <section class="card" aria-label="Business card">
    <svg class="card-arc" viewBox="0 0 780 444" aria-hidden="true">
      <path d="M -10 0 C 170 10, 318 150, 316 452" fill="none" stroke="var(--blush)" stroke-width="14"/>

      <!-- web icon -->
      <g class="icon-web" transform="translate(302 210)">
        <circle r="25" fill="var(--olive)" stroke="var(--blush)" stroke-width="6"/>
        <circle r="12" fill="none" stroke="var(--blush)" stroke-width="2.5"/>
        <ellipse rx="5" ry="12" fill="none" stroke="var(--blush)" stroke-width="2"/>
        <line x1="-12" y1="0" x2="12" y2="0" stroke="var(--blush)" stroke-width="2"/>
        <line x1="-10" y1="-6" x2="10" y2="-6" stroke="var(--blush)" stroke-width="1.6"/>
        <line x1="-10" y1="6" x2="10" y2="6" stroke="var(--blush)" stroke-width="1.6"/>
      </g>

      <!-- email icon -->
      <g class="icon-email" transform="translate(324 274)">
        <circle r="25" fill="var(--olive)" stroke="var(--blush)" stroke-width="6"/>
        <rect x="-12" y="-8" width="24" height="16" rx="2" fill="var(--blush)"/>
        <path d="M -12 -7 L 0 2 L 12 -7" fill="none" stroke="var(--olive)" stroke-width="2"/>
      </g>

      <!-- camera icon -->
      <g class="icon-camera" transform="translate(333 337)">
        <circle r="25" fill="var(--olive)" stroke="var(--blush)" stroke-width="6"/>
        <rect x="-11" y="-11" width="22" height="22" rx="6" fill="none" stroke="var(--blush)" stroke-width="2.5"/>
        <circle r="5" fill="none" stroke="var(--blush)" stroke-width="2.5"/>
      </g>
    </svg>

    <div class="brand">
      <div class="brand-name">torvin</div>
      <div class="brand-descriptor">psychology + EMDR</div>
    </div>
    <p class="tagline">Connect. Integrate. Evolve</p>

    <div class="person">
      <h1 class="person-name">Maren Holloway</h1>
      <p class="person-title">CLINICAL PSYCHOLOGIST</p>
    </div>

    <p class="contact contact-web">torvinpsychology.com.au</p>
    <p class="contact contact-email">hello@torvinpsychology.com.au</p>
    <p class="contact contact-social">@torvin.psychology.emdr</p>
  </section>
</body>
</html>
```